Plumbing business card and logo desgin

Need a new business card and logo for a plumbing business based in Warragul, Australia. Business name is 9Brook plumbing & air-conditioning. We service all plumbing and gasfitting needs and installation of air-conditioning. We clear blocked drains, install new hot water systems, central heating, new and existing homes, roofing, sanitary and drainage.
i would like to have a space on there for website, email, phone, licence number and what we do as a company.
i would like a water droplet to be incorporated into the design to try and stand out that we are a plumbing business

Contact Information for Business Card

phone number: 0497215836
Licence Number: 873614

Logo Text

9Brook Plumbing & Air-Conditioning

```html
<!DOCTYPE html>
<html lang="en">
<head>
<meta charset="utf-8">
<title>9Brook Plumbing &amp; Air-Conditioning – Business Card</title>
<link rel="stylesheet" href="https://fonts.googleapis.com/css2?family=Questrial&family=Montserrat:wght@600&display=swap">
<style>
  :root {
    --page: #ececec;
    --card: #f4f4f7;
    --brand-blue: #1a6fbf;
    --band-dark: #1d3d9e;
    --band-mid: #2a6cc0;
    --band-light: #1fa2e0;
    --ink: #2e2e2e;
    --ink-soft: #3c3c3c;
    --panel-tint: #c8d3ea;
    --panel-pale: #eceff6;
    --white: #ffffff;
  }
  * { box-sizing: border-box; margin: 0; padding: 0; }
  html, body { width: 1131px; height: 1200px; overflow: hidden; }
  body {
    background: var(--page);
    font-family: "Questrial", "Century Gothic", sans-serif;
    color: var(--ink);
    position: relative;
  }
  .card {
    position: absolute;
    width: 782px;
    height: 451px;
    background: var(--card);
    box-shadow: 0 14px 24px rgba(0,0,0,0.18);
    overflow: hidden;
  }
  .card--front { left: 178px; top: 102px; }
  .card--back  { left: 172px; top: 615px; }

  .droplet-field {
    position: absolute;
    inset: 0;
    background: radial-gradient(circle at 75% 40%, #e4ebf3 0%, #f2f4f7 45%, #f4f5f8 100%);
  }

  .brand {
    position: absolute;
    display: flex;
    flex-direction: column;
  }
  .brand__name {
    display: flex;
    align-items: center;
    gap: 14px;
    font-family: "Montserrat", sans-serif;
    font-weight: 600;
    font-size: 70px;
    line-height: 1;
    color: var(--brand-blue);
    letter-spacing: 1px;
  }
  .brand__mark {
    width: 44px; height: 44px;
    border-radius: 50%;
    background: var(--brand-blue);
  }
  .brand__tagline {
    font-size: 23px;
    color: var(--ink);
    margin-top: 8px;
    padding-left: 58px;
  }
  .card--front .brand { left: 52px; top: 92px; }
  .card--back .brand { left: 178px; top: 54px; }

  .contact {
    position: absolute;
    left: 58px;
    top: 296px;
    list-style: none;
    font-size: 23px;
    line-height: 32px;
    color: var(--ink-soft);
  }
  .contact__accent { color: var(--brand-blue); }

  .licence-band {
    position: absolute;
    left: 0; bottom: 0;
    width: 782px; height: 34px;
  }
  .licence-band__text {
    position: absolute;
    right: 44px; bottom: 3px;
    color: var(--white);
    font-size: 22px;
    letter-spacing: 0.5px;
  }

  .service-panel {
    position: absolute;
    left: 0; top: 0;
    width: 782px; height: 451px;
  }
  .services__title {
    position: absolute;
    left: 110px; top: 201px;
    width: 583px; height: 59px;
    border-radius: 30px;
    background: var(--brand-blue);
    color: var(--white);
    font-family: "Montserrat", sans-serif;
    font-weight: 600;
    font-size: 36px;
    display: flex;
    align-items: center;
    justify-content: center;
    letter-spacing: 0.5px;
  }
  .services__list {
    position: absolute;
    top: 290px;
    list-style: none;
    font-size: 23px;
    line-height: 33.5px;
    color: var(--ink-soft);
  }
  .services__list--left { left: 48px; }
  .services__list--right { left: 470px; }
  .services__list li {
    display: flex;
    align-items: center;
  }
  .services__list li::before {
    content: "";
    width: 13px; height: 13px;
    border-radius: 50%;
    background: var(--brand-blue);
    margin-right: 18px;
    flex: none;
  }
</style>
</head>
<body>

<section class="card card--front">
  <div class="droplet-field" role="img" aria-label="Water droplets scattered across a pale background"></div>

  <div class="brand">
    <div class="brand__name"><span class="brand__mark"></span>9Brook</div>
    <div class="brand__tagline">Plumbing &amp; Air-Conditioning</div>
  </div>

  <ul class="contact">
    <li>P:&nbsp; 0497215836</li>
    <li>m: info9brook@mailhub.com</li>
    <li>w: www.<span class="contact__accent">9brook</span>.com</li>
  </ul>

  <svg class="licence-band" viewBox="0 0 782 34" aria-hidden="true">
    <defs>
      <linearGradient id="bandDark" x1="0" x2="1">
        <stop offset="0" stop-color="var(--band-dark)"/>
        <stop offset="1" stop-color="var(--band-mid)"/>
      </linearGradient>
      <linearGradient id="bandLight" x1="0" x2="1">
        <stop offset="0" stop-color="var(--band-mid)"/>
        <stop offset="1" stop-color="var(--band-light)"/>
      </linearGradient>
    </defs>
    <polygon points="0,0 392,0 362,34 0,34" fill="url(#bandDark)"/>
    <polygon points="402,0 782,0 782,34 372,34" fill="url(#bandLight)"/>
  </svg>
  <span class="licence-band__text">Licence No: 873614</span>
</section>

<section class="card card--back">
  <svg class="service-panel" viewBox="0 0 782 451" aria-hidden="true">
    <polygon points="150,451 395,274 782,274 782,451" fill="var(--panel-pale)"/>
    <polygon points="395,274 782,274 782,392 232,392" fill="var(--panel-tint)"/>
  </svg>

  <div class="brand">
    <div class="brand__name"><span class="brand__mark"></span>9Brook</div>
    <div class="brand__tagline">Plumbing &amp; Air-Conditioning</div>
  </div>

  <h2 class="services__title">OUR SERVICE</h2>

  <ul class="services__list services__list--left">
    <li>installation of air-conditioning</li>
    <li>install new hot water systems</li>
    <li>plumbing and gasfitting</li>
    <li>new and existing homes</li>
  </ul>
  <ul class="services__list services__list--right">
    <li>sanitary and drainage</li>
    <li>clear blocked drains</li>
    <li>central heating</li>
    <li>roofing</li>
  </ul>
</section>

</body>
</html>
```